Lueur de Provins Immerse in the enchanting flavors of France at Lueur de Provins

A menu that is French in style with the Eiffel Tower. A elegant menu that is in rich blue with red or gold trimmings, we are a French Bakey and Cafe

Target Market(s)

30 to 55 people

Industry/Entity Type

Restaurant

Font styles to use
Decorative

Colors
0054AA
0677BA
7BADD7
CADEEF
E8F1F8
EB3D1F
EC4F4E
F09395
F8D3D4
FCEDEE

Requirements
Must have
• the attachment "My Brunch Specials" is the Menu I want you to create, it has all the text, "My Brunch Special Complete" is a word version. The menu size should be 4 1/4 wide by 14 inches long 2 Sided. must have our logo at the top , Make the font larger, because our biggest complaint about our menu is it is hard to read
Nice to have
• I would love to incorporate the Eiffel Tower as a silhouette in the background
Should not have
• I do not want too many pictures or small print

```html
<!DOCTYPE html>
<html lang="en">
<head>
<meta charset="utf-8">
<title>Lueur de Provins — Brunch &amp; Drink Specials</title>
<link rel="stylesheet" href="https://fonts.googleapis.com/css2?family=Great+Vibes&family=Alegreya:wght@500&family=Oswald:wght@400;500&family=Poppins:wght@300&display=swap">
<style>
  :root {
    --backdrop: #8f8f8f;
    --paper: #efedeb;
    --red: #eb3d1f;
    --red-soft: #f8d3d4;
    --red-pale: #fcedee;
    --navy: #1f2f55;
    --ink: #3a3a3a;
  }
  * { box-sizing: border-box; margin: 0; padding: 0; }
  html, body { width: 745px; height: 1200px; overflow: hidden; }
  body { background: var(--backdrop); position: relative; }

  .menu-side {
    position: absolute;
    top: 55px;
    width: 350px;
    height: 1090px;
    background: var(--paper);
    box-shadow: 0 6px 12px rgba(0,0,0,.35);
    overflow: hidden;
  }
  .menu-side--front { left: 15px; }
  .menu-side--back { left: 380px; }

  .frame {
    position: absolute;
    inset: 12px 13px;
    border: 1px solid var(--red);
    border-radius: 8px;
    pointer-events: none;
    z-index: 3;
  }

  .tower-art { position: absolute; z-index: 1; }
  .menu-side--front .tower-art {
    left: 14px; right: 14px; top: 745px; bottom: 0;
    background: radial-gradient(ellipse 40% 95% at 50% 100%, rgba(236,79,78,.38), rgba(248,211,212,.45) 55%, rgba(252,237,238,0) 100%);
  }
  .menu-side--back .tower-art {
    right: 0; width: 110px; top: 470px; bottom: 0;
    background: radial-gradient(ellipse 60% 100% at 70% 100%, rgba(248,211,212,.7), rgba(252,237,238,0) 100%);
  }

  .brand {
    position: absolute; top: 35px; left: 0; right: 0; z-index: 2;
    display: flex; flex-direction: column; align-items: center; gap: 12px;
  }
  .brand-mark { width: 30px; height: 30px; background: var(--navy); }
  .brand-name {
    font-family: "Oswald", sans-serif;
    font-weight: 400;
    font-size: 13px;
    letter-spacing: 6px;
    color: var(--navy);
    text-transform: uppercase;
  }

  .section-title {
    position: absolute; left: 0; right: 0; z-index: 2;
    text-align: center;
    font-family: "Great Vibes", cursive;
    font-weight: 400;
    font-size: 44px;
    line-height: 1;
    color: var(--red);
  }
  .section-title--main { top: 128px; }
  .section-title--minor { top: 712px; font-size: 38px; }

  .item-list {
    position: absolute; z-index: 2;
    left: 34px; right: 34px;
    display: flex; flex-direction: column; justify-content: space-between;
    text-align: center;
  }
  .menu-side--front .item-list--brunch { top: 183px; height: 555px; }
  .menu-side--back .item-list--drinks { top: 194px; height: 498px; }
  .menu-side--back .item-list--latte { top: 763px; height: 272px; }

  .item-head { display: flex; justify-content: center; align-items: baseline; gap: 9px; margin-bottom: 4px; }
  .item-name {
    font-family: "Alegreya", serif;
    font-weight: 500;
    font-size: 14px;
    line-height: 1.1;
    color: var(--red);
  }
  .item-price {
    font-family: "Oswald", sans-serif;
    font-weight: 500;
    font-size: 11.5px;
    color: var(--navy);
  }
  .item-desc {
    font-family: "Poppins", sans-serif;
    font-weight: 300;
    font-size: 8px;
    line-height: 1.2;
    color: var(--ink);
  }
</style>
</head>
<body>

<section class="menu-side menu-side--front">
  <div class="tower-art" role="img" aria-label="Red line illustration of the Eiffel Tower rising from the bottom of the menu, with faint tower outlines behind"></div>
  <div class="frame"></div>
  <header class="brand">
    <span class="brand-mark"></span>
    <span class="brand-name">Lueur de Provins</span>
  </header>
  <h1 class="section-title section-title--main">Brunch Specials</h1>

  <div class="item-list item-list--brunch">
    <article class="item">
      <div class="item-head"><h2 class="item-name">Ratatouille &amp; eggs</h2><span class="item-price">$18</span></div>
      <p class="item-desc">Experience the essence of Provence with our Ratatouille, a vibrant medley of roasted squash, peppers, tomatoes, eggplant, infused with fragrant fresh herbs. Served with two perfectly poached eggs, and your choice of flavorful andouille sausage or crispy bacon. Accompanied by a side of crusty baguette. It's a hearty dish that celebrates the flavors of the Mediterranean countryside.</p>
    </article>
    <article class="item">
      <div class="item-head"><h2 class="item-name">Le Grande Breakfast</h2><span class="item-price">$15</span></div>
      <p class="item-desc">Start your day in style with our Le Grande Breakfast, a feast fit for royalty. Customize your morning indulgence with two eggs cooked to your preference, paired with either savory bacon or succulent chicken sausage. Choose between a freshly baked baguette or a buttery croissant to accompany your meal. Complete your breakfast by selecting from an array of sides including crispy hash browns, savory roasted potatoes, or a refreshing fruit salad. Bon appetit!</p>
    </article>
    <article class="item">
      <div class="item-head"><h2 class="item-name">Smoked Salmon Tartine</h2><span class="item-price">$15</span></div>
      <p class="item-desc">Delight in the luxurious flavors of our Smoked Salmon Tartine, a culinary masterpiece that elevates breakfast to new heights. Indulge in truffled scrambled eggs nestled atop smoked salmon, adorned with tangy pickled red onions, briny caper berries, crisp cucumber, juicy tomato, and peppery arugula. All artfully arranged on multigrain bread generously spread with herb-infused cream cheese.</p>
    </article>
    <article class="item">
      <div class="item-head"><h2 class="item-name">Le Benedict Salmon</h2><span class="item-price">$15</span></div>
      <p class="item-desc">Savor the classic elegance of Eggs Benedict, featuring two perfectly poached eggs nestled on toasted English muffins, with luscious smoked salmon and ripe tomato slices crowned with a velvety lemon-infused Hollandaise sauce. A timeless brunch delight crafted to perfection.</p>
    </article>
    <article class="item">
      <div class="item-head"><h2 class="item-name">Salmon Atlantique</h2><span class="item-price">$15</span></div>
      <p class="item-desc">Enjoy a bed of crisp mixed greens adorned with delicate smoked salmon, sweet golden raisins, creamy goat cheese, and crunchy walnuts. All dressed in a tantalizing balsamic vinaigrette that ties the elements together perfectly.</p>
    </article>
    <article class="item">
      <div class="item-head"><h2 class="item-name">Beef Bourguignon</h2><span class="item-price">$15</span></div>
      <p class="item-desc">Indulge in our rich and comforting flavors of savory, tender beef slowly braised in red wine, creating a luscious sauce that envelops pearl onions, carrots, and mushrooms in a symphony of flavors. Served alongside buttered egg noodles. It's a hearty and soul-warming meal that promises pure culinary bliss.</p>
    </article>
    <article class="item">
      <div class="item-head"><h2 class="item-name">Tourte au Poulet</h2><span class="item-price">$15</span></div>
      <p class="item-desc">Discover the indulgent flavors of our Tourte au Poulet, a savory delight that marries tender marinated chicken with the richness of Swiss cheese and the sweetness of onions, all encased in layers of flaky pastry. Topped with a savory mushroom medley and decadent bechamel sauce. A true comfort classic to delight your senses.</p>
    </article>
  </div>
</section>

<section class="menu-side menu-side--back">
  <div class="tower-art" role="img" aria-label="Faint pink silhouette of the Eiffel Tower along the right edge"></div>
  <div class="frame"></div>
  <header class="brand">
    <span class="brand-mark"></span>
    <span class="brand-name">Lueur de Provins</span>
  </header>
  <h1 class="section-title section-title--main">Drink Specials</h1>

  <div class="item-list item-list--drinks">
    <article class="item">
      <div class="item-head"><h2 class="item-name">Bottomless Mimosa</h2><span class="item-price">$18</span></div>
      <p class="item-desc">Embark on an endless journey of delight with our Bottomless Mimosa, featuring Verlaine champagne, infusing each sip with a sparkling sensation. Tailor your experience with your preferred flavor profile - opt for the timeless twist of classic orange juice or tangy cranberry juice for a refreshing zing. Continuously poured to ensure your glass is always full.</p>
    </article>
    <article class="item">
      <div class="item-head"><h2 class="item-name">Apple Cider-Mimosa</h2><span class="item-price">$15</span></div>
      <p class="item-desc">A delightful twist on the classic mimosa. Crafted with champagne and crisp apple cider. To elevate the experience, we adorn the glass with a caramel rim dipped in brown sugar, adding a touch of indulgent sweetness to every sip.</p>
    </article>
    <article class="item">
      <div class="item-head"><h2 class="item-name">Blood Orange or Pineapple Spritz</h2><span class="item-price">$15</span></div>
      <p class="item-desc">Introducing our vibrant spritz cocktail, a tantalizing blend of Marlow &amp; Finch's premium Norvik Vodka, sweet vermouth, and a touch of sweetness from a carefully muddled sugar cube. This effervescent libation reaches new heights with the addition of bubbly Fontclair, your choice of either Blood Orange or Pineapple syrup injects a burst of fruity allure into every sip.</p>
    </article>
    <article class="item">
      <div class="item-head"><h2 class="item-name">Peach Bellini</h2><span class="item-price">$15</span></div>
      <p class="item-desc">Try our perfectly balanced Peach Bellini with each sip you capture the crispness of champagne with the irresistible sweetness of peach. It's a sublime fusion of sophistication and sweetness.</p>
    </article>
    <article class="item">
      <div class="item-head"><h2 class="item-name">Espresso Martini</h2><span class="item-price">$15</span></div>
      <p class="item-desc">Our Espresso Martini is a decadent blend of bold espresso, rich chocolate martini, and luxurious Valmont chocolate syrup. It's the ultimate indulgence for coffee and chocolate lovers alike.</p>
    </article>
    <article class="item">
      <div class="item-head"><h2 class="item-name">Kir Royale</h2><span class="item-price">$15</span></div>
      <p class="item-desc">Our Kir Royale is a delightful fusion of the crisp, sparkling champagne bubbles and the sweet sophistication of black currant. a luxurious and indulgent drink that's perfect for any occasion.</p>
    </article>
  </div>

  <h2 class="section-title section-title--minor">Latte</h2>

  <div class="item-list item-list--latte">
    <article class="item">
      <div class="item-head"><h2 class="item-name">Truffle Latte</h2><span class="item-price">$15</span></div>
      <p class="item-desc">We start with rich Valmont chocolate, known for its velvety smoothness and intense flavor. Then, we add a drizzle of salted caramel, adding a perfect balance of sweetness and a hint of savory richness. Finally, we combine this delightful blend with perfectly steamed milk to create a creamy and indulgent latte that will satisfy even the most discerning palate.</p>
    </article>
    <article class="item">
      <div class="item-head"><h2 class="item-name">Napoleon Latte</h2><span class="item-price">$15</span></div>
      <p class="item-desc">We start with our rich espresso, renowned for its bold and robust character. Then, we add a luscious combination of hazelnut and vanilla syrup, creating a symphony of sweetness and nutty richness. As the final touch, we crown this masterpiece with the velvety smoothness of perfectly steamed milk.</p>
    </article>
    <article class="item">
      <div class="item-head"><h2 class="item-name">Chai Latte</h2><span class="item-price">$15</span></div>
      <p class="item-desc">Our robust chai tea concentrate, infused with a symphony of cinnamon, cardamom, cloves, and ginger, sets the stage for a journey of aromatic delight. Paired with velvety steamed milk, each sip offers a harmonious blend of bold spices and creamy richness. Topped with a sprinkle of cinnamon, it's</p>
    </article>
  </div>
</section>

</body>
</html>
```